Eye-catching & Glamorous Labels for Skincare Bottles & Jars

We need new labels designed for our product range as we have been dormant for a few years and are now rebranding Velora Grace - Kindly Made Skincare. The label sizes are defined in the attached word document. All products have either a bright silver or a matte silver lid pump/spray so please keep this in mind.

We are open to colours and invite you to create bright trendy labels which are coordinated with the logo attached. The logo is not of any specific colour so dark on light, light on dark, tone on tone - we like purple / duck egg blue / turquoise WITH matte silver, however stronger colours like navy plus maroon with matte silver is also a strong favourite. If you feel inspired by a colour you think would be appropriate to Velora Grace please feel free to have a go.

A front section for product information is required and the back should include relevant details ie ingredients, company info, and a note that there has been no testing on animals.

The serum bottle will require a front and back label on a clear label in a pale colour to coordinate with the rest of the range. Size for this label is 35mm top edge, 25mm bottom edge, height 45mm - I have attached a picture of the serum bottle as they were originally pad printed. Please don't hesitate to contact me for any further information. Good luck!

Target Market(s)

Educated professional women 30-45 who are regular skincare users and looking for beautiful skincare products without animal derived ingredients and animal testing

Industry/Entity Type

Skin Care Product

Font styles to use
Serif
Sans Serif
Decorative
Script

Colors

Designer to choose colors to be used in the design.

Requirements
Must have
• Velora Grace Logo - eye catching design - not too busy or cramped.
Nice to have
• Is it possible to create a background pattern using a very small image of the logo? Just a thought.

```html
<!DOCTYPE html>
<html lang="en">
<head>
<meta charset="utf-8">
<title>Velora Grace – Power Lifting Day Cream Label</title>
<link rel="stylesheet" href="https://fonts.googleapis.com/css2?family=Cinzel+Decorative:wght@400;700&family=Lato:wght@300;400;700;900&display=swap">
<style>
  :root {
    --bg-top: #dcdcdc;
    --bg-bottom: #ffffff;
    --taupe: #aea69f;
    --gold: #ecb24f;
    --grey-text: #5a5a5a;
    --dark-text: #3e3e3e;
    --badge-line: #8f8f8f;
    --pattern-gold: #f2cf84;
    --pattern-grey: #cfcac5;
  }
  html, body {
    margin: 0;
    padding: 0;
    overflow: hidden;
  }
  .label {
    position: relative;
    width: 1200px;
    height: 811px;
    overflow: hidden;
    background: linear-gradient(to bottom, var(--bg-top) 0%, #eeeeee 35%, var(--bg-bottom) 75%);
    font-family: "Lato", Arial, sans-serif;
  }

  /* Front panel */
  .brand {
    position: absolute;
    left: 415px;
    top: 120px;
    width: 400px;
    text-align: center;
  }
  .brand-mark {
    display: block;
    width: 46px;
    height: 46px;
    margin: 0 auto 18px;
    border-radius: 50%;
    background: var(--taupe);
  }
  .brand-name {
    font-family: "Lato", Arial, sans-serif;
    font-weight: 400;
    font-size: 52px;
    letter-spacing: 2px;
    color: var(--taupe);
    line-height: 1;
  }
  .product-title {
    position: absolute;
    left: 365px;
    top: 350px;
    width: 500px;
    margin: 0;
    text-align: center;
    font-family: "Cinzel Decorative", "Times New Roman", serif;
    font-weight: 400;
    font-size: 58px;
    line-height: 56px;
    letter-spacing: 2px;
    color: var(--gold);
  }
  .product-type {
    position: absolute;
    left: 365px;
    top: 468px;
    width: 500px;
    text-align: center;
    font-family: "Lato", Arial, sans-serif;
    font-weight: 300;
    font-size: 42px;
    letter-spacing: 1px;
    color: var(--taupe);
  }
  .ornament {
    position: absolute;
    left: 600px;
    top: 548px;
    width: 32px;
    height: 32px;
    background: var(--gold);
    opacity: 0.8;
    border-radius: 4px;
  }

  /* Back panel */
  .details {
    position: absolute;
    left: 865px;
    top: 54px;
    width: 280px;
    color: var(--grey-text);
  }
  .ingredients-heading {
    margin: 0;
    font-size: 15px;
    font-weight: 700;
    color: var(--dark-text);
    letter-spacing: 0.5px;
  }
  .ingredients-text {
    margin: 2px 0 0;
    font-size: 14px;
    line-height: 18.9px;
    font-weight: 400;
  }
  .cruelty-badge {
    display: flex;
    align-items: center;
    justify-content: space-between;
    width: 268px;
    height: 60px;
    margin-top: 20px;
    padding: 0 6px 0 16px;
    box-sizing: border-box;
    border: 2px solid var(--badge-line);
    border-radius: 32px;
  }
  .cruelty-badge p {
    margin: 0;
    font-size: 13.5px;
    line-height: 16px;
    font-weight: 900;
    color: var(--dark-text);
  }
  .certificate-seal {
    width: 48px;
    height: 48px;
    border-radius: 50%;
    background: var(--badge-line);
  }
  .address {
    margin: 24px 0 0;
    font-size: 14px;
    line-height: 18px;
    font-style: normal;
  }
  .volume {
    margin: 26px 0 0;
    font-size: 14px;
    line-height: 18px;
    font-weight: 700;
  }
  .origin {
    margin: 6px 0 0;
    font-size: 14px;
    font-weight: 700;
  }

  /* Bottom pattern band */
  .pattern-band {
    position: absolute;
    left: 0;
    bottom: 0;
    width: 1200px;
    height: 134px;
    background: linear-gradient(90deg, var(--pattern-grey), var(--pattern-gold), var(--pattern-grey), var(--pattern-gold), var(--pattern-grey));
    opacity: 0.75;
  }
</style>
</head>
<body>
  <main class="label">
    <div class="brand">
      <span class="brand-mark"></span>
      <div class="brand-name">Velora Grace</div>
    </div>

    <h1 class="product-title">POWER<br>LIFTING</h1>
    <div class="product-type">DAY CREAM</div>
    <div class="ornament" role="img" aria-label="Small four-petal gold ornament"></div>

    <section class="details">
      <h2 class="ingredients-heading">INGREDIENT</h2>
      <p class="ingredients-text">Quisque vitae ex et odio aliquam varius eu non augue. Maecenas lobortis tellus at tortor venenatis rhoncus. Ut elit eros, pellentesque sed magna et, posuere convallis sem. Duis id ligula malesuada, elementum quam sit amet, mollis massa. Donec ultricies arcu aliquet sapien ornare, at dictum leo convallis. Phasellus urna metus, ornare sit amet consectetur quis, porttitor sed felis. Donec in ipsum varius, hendrerit justo in, faucibus lectus. Curabitur ultrices, elit in finibus rutrum, dolor mi pharetra tellus, quis vestibulum ex dui non diam. Sed viverra interdum malesuada. Morbi aliquam, lectus et tincidunt iaculis, diam elit vestibulum magna, suscipit sollicitudin nisi lectus id nisl. Curabitur nec malesuada lorem.</p>

      <div class="cruelty-badge">
        <p>WE GUARANTEE OUR<br>PRODUCTS WITHOUT<br>TESTING ON ANIMALS</p>
        <span class="certificate-seal"></span>
      </div>

      <address class="address">2186 W. Marigold Grove Ave.<br>Seabrook, FL 33921</address>
      <p class="volume">100ml (3.3US FL OZ)</p>
      <p class="origin">MADE IN USA</p>
    </section>

    <div class="pattern-band" role="img" aria-label="Repeating pattern of gold and grey four-petal flowers in a lattice"></div>
  </main>
</body>
</html>
```